KVT Business Cards

We require business cards for our business. We would like a matte black back to the card, with our logo centred in the middle. The front side of the card is open to design.

Target Market(s)

Clients looking for legal services (professional)

Industry/Entity Type

Legal

Contact Information for Business Card

Boris Telemark
Partner
Mobile: 0438 715 642
Email: boris@kvtlaw.co
Website: www.kvtlaw.co
Level 3, 118 Wexbury Street
Sydney NSW 2000

Font styles to use
Other font styles liked:
• Avenir

Colors
f04a50
ffffff
1b1b1b

Requirements
Must have
• Black back with logo included in the centre of the card.
• Our font is Avenir.

```html
<!DOCTYPE html>
<html lang="en">
<head>
<meta charset="utf-8">
<title>KVT Business Cards</title>
<link rel="stylesheet" href="https://fonts.googleapis.com/css2?family=Nunito+Sans:wght@400;700;800&display=swap">
<style>
  :root {
    --stage: #3b4448;
    --card: #070808;
    --ink: #ffffff;
    --accent: #ee3a62;
    --accent-deep: #8c0a2c;
    --accent-bright: #dc0a4c;
    --watermark: #151515;
    --font: "Nunito Sans", "Avenir", sans-serif;
  }
  * { margin: 0; padding: 0; box-sizing: border-box; }
  html, body {
    width: 1200px; height: 1200px; overflow: hidden;
    background: var(--stage);
    font-family: var(--font);
  }
  .card {
    position: absolute; left: 117px; width: 965px; height: 553px;
    background: var(--card); overflow: hidden;
  }
  .card--front { top: 37px; }
  .card--back { top: 618px; }

  .side-band {
    position: absolute; left: 0; top: 0; width: 40px; height: 274px;
    background: linear-gradient(180deg, var(--accent-bright), var(--accent-deep));
  }
  .foot-band {
    position: absolute; right: 0; bottom: 0; width: 383px; height: 16px;
    background: var(--ink);
  }

  .rule { position: absolute; left: 52px; width: 397px; height: 3px; background: var(--accent-bright); }

  .holder-name {
    position: absolute; left: 73px; top: 72px;
    font-weight: 800; font-size: 42px; letter-spacing: 0.5px; color: var(--ink);
    line-height: 1;
  }
  .holder-name .surname { color: var(--accent); }
  .holder-role {
    position: absolute; left: 73px; top: 125px;
    font-size: 26px; font-weight: 400; color: var(--ink); line-height: 1;
  }
  .address {
    position: absolute; left: 76px; top: 194px;
    font-size: 25px; color: var(--ink); line-height: 37px; letter-spacing: 0.4px;
  }
  .contact {
    position: absolute; left: 74px; display: flex; align-items: center; gap: 12px;
    font-size: 25px; color: var(--accent); letter-spacing: 0.3px; line-height: 1;
  }
  .contact svg { width: 26px; height: 26px; flex: none; }
  .contact--phone { top: 314px; }
  .contact--email { top: 377px; }
  .contact--web { top: 435px; }

  .firm-watermark {
    position: absolute; left: 581px; top: 196px;
    font-weight: 800; font-size: 52px; line-height: 59px; color: var(--watermark);
    text-transform: uppercase;
  }

  .brand {
    position: absolute; left: 0; top: 0; width: 100%; height: 100%;
    display: flex; align-items: center; justify-content: center; gap: 60px;
  }
  .brand-mark { width: 110px; height: 110px; background: var(--accent); }
  .brand-name {
    font-weight: 800; font-size: 56px; line-height: 58px; color: var(--ink);
    text-transform: uppercase;
  }
</style>
</head>
<body>
  <section class="card card--front">
    <div class="side-band"></div>

    <h1 class="holder-name">BORIS <span class="surname">TELEMARK</span></h1>
    <p class="holder-role">PARTNER</p>

    <div class="rule" style="top:183px"></div>
    <p class="address">Level 3, 118 Wexbury Street<br>Sydney NSW 2000</p>
    <div class="rule" style="top:270px"></div>

    <p class="contact contact--phone">
      <svg viewBox="0 0 24 24" aria-hidden="true"><path fill="#ffffff" d="M7 1h10a2 2 0 0 1 2 2v18a2 2 0 0 1-2 2H7a2 2 0 0 1-2-2V3a2 2 0 0 1 2-2zm0 3v14h10V4zm5 15.3a1.2 1.2 0 1 0 0 2.4 1.2 1.2 0 0 0 0-2.4z"/></svg>
      0438 715 642
    </p>
    <p class="contact contact--email">
      <svg viewBox="0 0 24 24" aria-hidden="true"><path fill="#ffffff" d="M2 5h20v1.5l-10 6.5L2 6.5zm0 3.8l10 6.4 10-6.4V19H2z"/></svg>
      boris@kvtlaw.co
    </p>
    <p class="contact contact--web">
      <svg viewBox="0 0 24 24" aria-hidden="true" fill="none" stroke="#ffffff" stroke-width="2"><circle cx="12" cy="12" r="10"/><ellipse cx="12" cy="12" rx="4.5" ry="10"/><path d="M2 12h20"/></svg>
      www.kvtlaw.co
    </p>

    <p class="firm-watermark">Kovach<br>Vale<br>Telemark</p>

    <div class="foot-band"></div>
  </section>

  <section class="card card--back">
    <div class="brand">
      <div class="brand-mark"></div>
      <p class="brand-name">Kovach<br>Vale<br>Telemark</p>
    </div>
  </section>
</body>
</html>
```